Feng shui business card for immigration law firm

Immigration law firm would like to create the business card based and look like the Green Card (lawful permanent resident card of USA). Attached please see the sample of American Green Card. The whole business card should be performed based on the FENG SHUI style: no sharp angles. Please delete all letters and fingerprint on the sample green card and put info the following order.
Updates

Project Deadline Extended
Reason: needs more time and designs to choose from

Target Market(s)

Immigration clients in USA

Industry/Entity Type

Business

Contact Information for Business Card

Immigration law firm would like to create the business card based and look like the Green Card (lawful permanent resident card of USA). Attached please see the sample of American Green Card. The whole business card should be performed based on the FENG SHUI style: no sharp angles. Please delete all letters on sample green card and put info the following order:

TOVAR ELSKINDO, ESQ.
ELSKINDO LAW GROUP, P.A.
PRACTICE LIMITED TO IMMIGRATION LAW

4716 WEST PERRICOTT GROVE BOULVERD
SUITE #218
HALLANDALE BEACH, FLORIDA 33021

PHONE: 754-555-0162
EMAIL: TELSKINDO@QUORVELMAIL.COM
WEBSITE: WWW.VANTREL-VISALAW.COM

The tips for the best business card
1. It is recommended to avoid using sharp points in the logo because such logos generate negative energy. Never use sharp and pointed element like spears, knives or swords in your logo.
2. One of the most essential elements in Feng Shui good flow and space which means that there should not be any obstruction, for example, there should not be any border around the card as it stop the energy flow.
3. Keep clear of clutter – Just like applying this feng shui concept to home and office, it should also be applied to designing your name card. Always keep your card as clean and concise as possible by removing all redundant information and put only relevant ones.
4. Name should not be placed in the center of the card because it cause stress and pressure to the owner.

Font styles to use
Other font styles liked:
• Garamond or Times New Roman

Requirements
Must have
• Feng shui business card

```html
<!DOCTYPE html>
<html lang="en">
<head>
<meta charset="utf-8">
<title>Elskindo Law Group – Business Card</title>
<link href="https://fonts.googleapis.com/css2?family=Tinos:wght@400;700&display=swap" rel="stylesheet">
<style>
  :root {
    --stage: #e8e5e0;
    --paper: #fbfbfb;
    --ink: #1b1b1b;
    --red: #c8161d;
    --red-deep: #a90f15;
    --black: #070707;
    --white: #ffffff;
  }
  * { box-sizing: border-box; margin: 0; padding: 0; }
  html, body { width: 1200px; height: 892px; overflow: hidden; }
  body {
    background: var(--stage);
    font-family: "Tinos", "Times New Roman", serif;
    color: var(--ink);
    position: relative;
  }
  .card {
    position: absolute;
    top: 292px;
    width: 540px;
    height: 308px;
    border-radius: 10px;
    overflow: hidden;
    box-shadow: 0 6px 18px rgba(0,0,0,.18);
  }
  /* Front */
  .card--front { left: 40px; background: var(--paper); }
  .firm-name {
    position: absolute; left: 40px; top: 26px;
    font-size: 36px; font-weight: 400; letter-spacing: .2px; white-space: nowrap;
  }
  .firm-tagline {
    position: absolute; left: 62px; top: 72px;
    font-size: 17px; white-space: nowrap;
  }
  .brand-mark {
    position: absolute; left: 28px; top: 112px;
    width: 140px; height: 110px;
    display: flex; align-items: center; justify-content: center; gap: 8px;
  }
  .brand-mark__dot { width: 14px; height: 14px; border-radius: 50%; background: var(--red); flex: none; }
  .brand-mark__name { font-size: 17px; color: var(--red); line-height: 1.15; }
  .divider {
    position: absolute; left: 184px; top: 104px;
    width: 1.5px; height: 130px;
    background: linear-gradient(to bottom, rgba(0,0,0,0), var(--ink) 25%, var(--ink) 75%, rgba(0,0,0,0));
  }
  .person { position: absolute; left: 204px; top: 104px; }
  .person__name { font-size: 24px; color: var(--red); white-space: nowrap; }
  .person__title { font-size: 19px; margin-top: 2px; }
  .contacts { position: absolute; left: 204px; top: 172px; list-style: none; }
  .contacts li {
    display: flex; align-items: center; gap: 9px;
    font-size: 15.5px; line-height: 22px; white-space: nowrap;
  }
  .icon {
    width: 13px; height: 13px; border-radius: 2px; background: var(--red);
    display: flex; align-items: center; justify-content: center; flex: none;
  }
  .icon svg { width: 9px; height: 9px; }
  .address-band {
    position: absolute; left: 0; right: 0; bottom: 0; height: 50px;
    background: linear-gradient(to bottom, var(--red), var(--red-deep));
    display: flex; align-items: center; gap: 8px; padding-left: 16px;
    color: var(--white); font-size: 14.5px; white-space: nowrap;
  }
  .address-band .icon { background: var(--white); }
  /* Back */
  .card--back {
    left: 620px;
    background: linear-gradient(150deg, #1a1a1a 0%, var(--black) 45%, #111 100%);
    display: flex; align-items: center; justify-content: center;
  }
  .back-mark { display: flex; align-items: center; gap: 12px; }
  .back-mark__dot { width: 22px; height: 22px; border-radius: 50%; background: var(--red); }
  .back-mark__name { font-size: 30px; color: var(--white); white-space: nowrap; }
</style>
</head>
<body>
  <section class="card card--front" aria-label="Business card front">
    <h1 class="firm-name">Elskindo Law Group, P.A</h1>
    <p class="firm-tagline">Practice Limited to Immigration Law</p>

    <div class="brand-mark">
      <span class="brand-mark__dot"></span>
      <span class="brand-mark__name">Elskindo<br>Law Group</span>
    </div>

    <div class="divider"></div>

    <div class="person">
      <p class="person__name">Tovar Elskindo</p>
      <p class="person__title">ESQ</p>
    </div>

    <ul class="contacts">
      <li><span class="icon"><svg viewBox="0 0 10 10"><path d="M2 1l2 2-1 1.2a6 6 0 0 0 2.8 2.8L7 6l2 2-1.2 1.3C4.5 9 1 5.5.7 2.2z" fill="#fff"/></svg></span>754-555-0162</li>
      <li><span class="icon"><svg viewBox="0 0 10 10"><rect x="1" y="2.5" width="8" height="5.5" rx=".6" fill="none" stroke="#fff" stroke-width="1"/><path d="M1.3 3l3.7 2.7L8.7 3" fill="none" stroke="#fff" stroke-width="1"/></svg></span>Telskindo@Quorvelmail.com</li>
      <li><span class="icon"><svg viewBox="0 0 10 10"><circle cx="5" cy="5" r="3.8" fill="none" stroke="#fff" stroke-width="1"/><path d="M1.2 5h7.6M5 1.2c-2 2.3-2 5.3 0 7.6M5 1.2c2 2.3 2 5.3 0 7.6" fill="none" stroke="#fff" stroke-width=".8"/></svg></span>www.Vantrel-visalaw.com</li>
    </ul>

    <div class="address-band">
      <span class="icon"><svg viewBox="0 0 10 10"><path d="M5 1.2L1 4.8h1.3V9h2.2V6.4h1V9h2.2V4.8H9z" fill="#c8161d"/></svg></span>
      4716 West Perricott Grove Boulverd suite #218 Hallandale Beach, Florida 33021
    </div>
  </section>

  <section class="card card--back" aria-label="Business card back">
    <div class="back-mark">
      <span class="back-mark__dot"></span>
      <span class="back-mark__name">Elskindo Law Group</span>
    </div>
  </section>
</body>
</html>
```